Business Card for Makeup Artist

I need a business card designed for my makeup and hair artistry business which is primarily events and weddings focused. The card needs to be sleek, simple, stylish and appealing to women. I would prefer a white background but open to suggestions also. I also love the marble background look. I have attached some example pics. It needs to be a double sided card with logo and/or design on one side and contact details in the centre of the card on the other side. NO LOGO ON BACK. Examples attached.

Target Market(s)

Females age 14-55

Industry/Entity Type

Business

Contact Information for Business Card

Nora Vint
Principal Makeup Artist
P: 0413 925 214
E: nora@lumirabeauty.com.au
W: www.lumirabeauty.com.au

Requirements
Should not have
• No yellow, green, red or blue in the design.

```html
<!DOCTYPE html>
<html lang="en">
<head>
<meta charset="utf-8">
<title>Lumira Makeup Artistry – Business Card</title>
<link rel="stylesheet" href="https://fonts.googleapis.com/css2?family=Cormorant+Garamond:wght@400;500&family=Great+Vibes&display=swap">
<style>
  :root {
    --backdrop: #8c8c8c;
    --card: #fdfcf8;
    --ink: #4f4f4f;
    --ink-soft: #6a6a6a;
    --rule: #9a9a9a;
    --bloom-pink: #efc3d8;
    --bloom-rose: #e6a9c6;
    --bloom-lilac: #d7c2e6;
    --bloom-mauve: #c9a9d8;
  }
  * { box-sizing: border-box; margin: 0; padding: 0; }
  html, body {
    width: 802px;
    height: 1200px;
    overflow: hidden;
  }
  body {
    position: relative;
    background: var(--backdrop);
    font-family: "Cormorant Garamond", Georgia, serif;
    color: var(--ink);
  }
  .card {
    position: absolute;
    left: 61px;
    width: 680px;
    height: 420px;
    background: var(--card);
    overflow: hidden;
    box-shadow: 0 2px 8px rgba(0, 0, 0, 0.18);
  }
  .card--front { top: 150px; }
  .card--back  { top: 640px; }

  .floral-band {
    position: absolute;
    left: 0;
    right: 0;
    bottom: 0;
    background:
      radial-gradient(ellipse 30% 70% at 18% 85%, var(--bloom-rose) 0%, rgba(230, 169, 198, 0) 70%),
      radial-gradient(ellipse 26% 60% at 55% 90%, var(--bloom-pink) 0%, rgba(239, 195, 216, 0) 70%),
      radial-gradient(ellipse 28% 65% at 86% 80%, var(--bloom-mauve) 0%, rgba(201, 169, 216, 0) 70%),
      linear-gradient(to bottom, rgba(253, 252, 248, 0) 0%, var(--bloom-lilac) 55%, var(--bloom-pink) 100%);
  }
  .card--front .floral-band { height: 190px; }
  .card--back .floral-band  { height: 150px; }

  /* Front */
  .brand {
    position: absolute;
    top: 60px;
    left: 0;
    right: 0;
    text-align: center;
    z-index: 1;
  }
  .brand__name {
    font-family: "Great Vibes", cursive;
    font-weight: 400;
    font-size: 118px;
    line-height: 1;
    color: var(--ink);
  }
  .brand__tagline {
    margin-top: 2px;
    font-size: 30px;
    letter-spacing: 0.12em;
    text-transform: uppercase;
    color: var(--ink-soft);
  }

  /* Back */
  .contact {
    position: absolute;
    top: 30px;
    left: 0;
    right: 0;
    text-align: center;
    z-index: 1;
  }
  .contact__name {
    font-family: "Great Vibes", cursive;
    font-size: 48px;
    line-height: 1.1;
    color: var(--ink);
  }
  .contact__role {
    margin-top: 6px;
    font-size: 24px;
    font-weight: 500;
    font-variant: small-caps;
    letter-spacing: 0.1em;
    color: var(--ink);
  }
  .contact__rule {
    width: 360px;
    height: 1px;
    margin: 8px auto 0;
    background: var(--rule);
  }
  .contact__details {
    list-style: none;
    margin-top: 36px;
    font-size: 21px;
    font-variant: small-caps;
    letter-spacing: 0.08em;
    line-height: 1.3;
    color: var(--ink);
  }
</style>
</head>
<body>

  <section class="card card--front" aria-label="Card front">
    <div class="brand">
      <p class="brand__name">Lumira</p>
      <p class="brand__tagline">Makeup Artistry</p>
    </div>
    <div class="floral-band" role="img" aria-label="Watercolour pink and lilac peony flowers along the bottom edge"></div>
  </section>

  <section class="card card--back" aria-label="Card back">
    <div class="contact">
      <h1 class="contact__name">Nora Vint</h1>
      <p class="contact__role">Principal Makeup Artist</p>
      <div class="contact__rule"></div>
      <ul class="contact__details">
        <li>P: 0413 925 214</li>
        <li>E: nora@lumirabeauty.com.au</li>
        <li>W: www.lumirabeauty.com.au</li>
      </ul>
    </div>
    <div class="floral-band" role="img" aria-label="Watercolour pink and lilac peony flowers along the bottom edge"></div>
  </section>

</body>
</html>
```